Graphic Design Project-Label for New Bourbon

Hi Designers

This is a new label for a Bourbon .Im looking for a smart looking label, Mordern,Simple .Clean.

Bottle type is the same as Harlow Gin Bottle if you google or can use others bottles glass.

I am open to new bourbon names and would love to see your creativity.

The Label Name is currently called Copper Ridge
Size is 1 litre.
Percentage is 37.5%.
Updates

Target Market(s)

ALL bourbon drinkers

Industry/Entity Type

Graphic Design

Requirements
Must have
• Up on top chosen label will send ingrediance final changes

```html
<!DOCTYPE html>
<html lang="en">
<head>
<meta charset="utf-8">
<title>Copper Ridge – Straight Bourbon Whisky Label</title>
<link rel="stylesheet" href="https://fonts.googleapis.com/css2?family=Libre+Baskerville:wght@400;700&family=Pinyon+Script&display=swap">
<style>
  :root {
    --page: #ffffff;
    --paper-light: #f1ebdd;
    --paper-dark: #e4d9c3;
    --ink: #231712;
    --ink-soft: #3b2c22;
    --accent-red: #8c1f1a;
    --compass-tone: #b9ab93;
  }
  html, body {
    margin: 0;
    padding: 0;
    width: 906px;
    height: 1200px;
    overflow: hidden;
    background: var(--page);
  }
  .label {
    position: absolute;
    left: 93px;
    top: 57px;
    width: 720px;
    height: 1086px;
    background: linear-gradient(160deg, var(--paper-light) 0%, var(--paper-dark) 100%);
    color: var(--ink);
    font-family: "Libre Baskerville", Georgia, serif;
    text-align: center;
  }
  .label__category {
    position: absolute;
    left: 0;
    top: 70px;
    width: 720px;
    height: 110px;
    overflow: visible;
  }
  .label__category text {
    font-family: "Libre Baskerville", Georgia, serif;
    font-size: 26px;
    fill: var(--ink);
    letter-spacing: 0.5px;
  }
  .label__brand {
    position: absolute;
    left: 0;
    top: 200px;
    width: 100%;
    margin: 0;
    font-weight: 700;
    font-size: 84px;
    line-height: 96px;
    letter-spacing: 3px;
    color: var(--ink);
  }
  .label__age {
    position: absolute;
    left: 0;
    top: 465px;
    width: 100%;
    margin: 0;
    font-size: 38px;
    color: var(--ink-soft);
    letter-spacing: 1px;
  }
  .label__age-number {
    font-size: 96px;
    color: var(--accent-red);
    vertical-align: -12px;
    margin: 0 8px;
  }
  .label__maker-script {
    position: absolute;
    left: 0;
    top: 596px;
    width: 100%;
    margin: 0;
    font-family: "Pinyon Script", cursive;
    font-size: 30px;
    color: var(--ink-soft);
  }
  .label__compass {
    position: absolute;
    left: 275px;
    top: 650px;
    width: 170px;
    height: 220px;
    border-radius: 50%;
    background: radial-gradient(circle, var(--ink-soft) 0%, var(--compass-tone) 45%, transparent 72%);
  }
  .label__description {
    position: absolute;
    left: 125px;
    top: 890px;
    width: 470px;
    margin: 0;
    font-size: 18px;
    line-height: 24px;
    color: var(--ink);
  }
  .label__footer {
    position: absolute;
    left: 50px;
    right: 50px;
    top: 1010px;
    display: flex;
    justify-content: space-between;
    align-items: flex-start;
    font-size: 22px;
    color: var(--ink);
  }
  .label__footer-maker {
    font-size: 18px;
    line-height: 24px;
    letter-spacing: 0.5px;
  }
  .label__abv, .label__volume {
    padding-top: 10px;
  }
</style>
</head>
<body>
  <main class="label">
    <svg class="label__category" viewBox="0 0 720 110" aria-label="Straight Bourbon Whisky">
      <path id="category-arc" d="M60 100 Q360 30 660 100" fill="none"/>
      <text><textPath href="#category-arc" startOffset="50%" text-anchor="middle">STRAIGHT BOURBON WHISKY</textPath></text>
    </svg>

    <h1 class="label__brand">COPPER<br>RIDGE</h1>

    <p class="label__age">AGED<span class="label__age-number">15</span>YEARS</p>

    <p class="label__maker-script">distilled, blended &amp; bottled by</p>

    <div class="label__compass" role="img" aria-label="Compass rose emblem with N, E, S, W markings"></div>

    <p class="label__description">Lorem ipsum dolor sit amet, consectetuer adipiscing elit, sed diam nonummy nibh euismod tincidunt ut laoreet dolore magna aliquam erat volutpat.</p>

    <footer class="label__footer">
      <span class="label__abv">37.5%</span>
      <span class="label__footer-maker">DISTILLED, BLENDED &amp; BOTTLED BY<br>ABC COMPANY</span>
      <span class="label__volume">1 Litre</span>
    </footer>
  </main>
</body>
</html>
```